TBNW site redesign

Please redesign a home page with content provided. PSD only - no coding
Can use any images from Vexelmarq.com

Please create a site design that more clearly illustrates the client's services and expertise. We are looking for a high-end design.

Any images used must be generic or of Dallas TX.

Fonts: Any
Colors: Match to logo
Look: Modern - Professional

Target Market(s)

medium-large business owners

Number of Pages Required

1 page

Font styles to use
Serif
Sans Serif

Requirements
Must have
• cohesive professional design
• high end look
• Match to logo

```html
<!DOCTYPE html>
<html lang="en">
<head>
<meta charset="utf-8">
<title>TBNW – Commercial Tenant Representation, Dallas TX</title>
<link rel="stylesheet" href="https://fonts.googleapis.com/css2?family=Tinos:wght@400;700&family=Open+Sans:wght@400;600&display=swap">
<style>
:root{
  --red:#c4070b;
  --red-dark:#9e0307;
  --ink:#222222;
  --muted:#555555;
  --line:#dddddd;
  --panel:#f1f1f1;
  --footer:#2f2f2f;
  --white:#ffffff;
  --serif:'Tinos', 'Times New Roman', serif;
  --sans:'Open Sans', Arial, sans-serif;
}
*{box-sizing:border-box;margin:0;padding:0}
html,body{width:1200px;height:3327px;overflow:hidden;background:var(--white)}
body{font-family:var(--serif);color:var(--ink);position:relative}
.page{position:relative;width:1200px;height:3327px}
.abs{position:absolute}
a{color:inherit;text-decoration:none}
ul{list-style:none}
h1,h2,h3,h5{font-weight:400}

/* top bar */
.topbar{left:0;top:0;width:1200px;height:124px}
.topbar__contact{top:48px;font-size:15px;display:flex;align-items:center;gap:8px}
.topbar__mail{left:122px;color:var(--ink)}
.topbar__phone{right:122px;color:var(--red)}
.brand{display:flex;align-items:center;gap:10px;font-family:var(--serif);font-size:34px;line-height:1;font-weight:400}
.brand__mark{width:18px;height:18px;display:block}
.brand--header{left:0;width:1200px;top:42px;justify-content:center;color:var(--red)}
.brand--header .brand__mark{background:var(--red)}
.brand--footer{left:122px;top:92px;color:var(--white)}
.brand--footer .brand__mark{background:var(--red)}

/* nav */
.nav{left:0;top:126px;width:1200px;height:42px;background:var(--red)}
.nav__item{top:0;height:42px;line-height:42px;color:var(--white);font-size:14px}
.nav__item--active{background:var(--red-dark);padding:0 32px}
.nav__search{left:858px;top:7px;width:222px;height:28px;background:var(--white);font-size:13px;color:var(--muted);padding:0 10px;line-height:28px}
.nav__search svg{position:absolute;right:7px;top:6px}

/* hero */
.hero{left:0;top:170px;width:1200px;height:588px;background:linear-gradient(180deg,#8d8b86 0%,#6e6a63 28%,#4a4540 60%,#2e2a27 100%)}
.hero__title{left:0;width:1200px;top:406px;text-align:center;color:var(--white);font-size:37px;line-height:40px}
.hero__lead{left:0;width:1200px;top:489px;text-align:center;color:var(--white);font-size:15px}
.hero__dots{left:568px;top:650px;display:flex;gap:8px}
.hero__dots span{width:10px;height:10px;border-radius:50%;background:var(--white)}
.hero__dots span.on{background:var(--red)}
.hero__arrow{width:30px;height:30px;border-radius:50%;background:var(--white)}

.btn{display:block;background:var(--red);color:var(--white);text-align:center;border-radius:20px;font-size:14px}
.btn--hero{left:526px;top:522px;width:148px;height:38px;line-height:38px}
.btn--mid{left:527px;width:146px;height:38px;line-height:38px}

/* search panel */
.finder{left:122px;top:683px;width:958px;height:144px;background:var(--red)}
.finder__select{top:27px;height:38px;background:var(--white);border-radius:4px;font-family:var(--sans);font-size:12px;color:var(--muted);padding:0 12px;line-height:38px}
.finder__select svg{position:absolute;right:10px;top:13px}
.finder__go{top:27px;left:810px;width:131px;height:38px;background:#333;border-radius:4px;color:var(--white);font-family:var(--sans);font-size:12px;line-height:38px;padding-left:56px}
.finder__go svg{position:absolute;left:16px;top:12px}
.finder__price{left:20px;top:80px;color:var(--white);font-size:13px}
.finder__adv{right:20px;top:80px;color:var(--white);font-size:13px;text-decoration:underline}
.finder__track{left:24px;top:109px;width:910px;height:3px;background:var(--white)}
.finder__knob{top:101px;width:18px;height:18px;border-radius:50%;background:var(--white)}

/* intro */
.headline{left:0;width:1200px;text-align:center;font-size:33px;color:var(--ink)}
.copy{left:0;width:1200px;text-align:center;font-size:14px;line-height:19px;color:var(--muted)}

/* tabs */
.tabs{left:0;width:1200px;display:flex;justify-content:center;font-size:17px;color:var(--muted)}
.tabs span{padding:0 12px}
.tabs i{font-style:normal;color:#aaa}
.tabs .on{color:var(--red)}
.pager{top:1216px;display:flex;gap:6px}
.pager span{width:24px;height:24px;border-radius:50%;display:block}

/* property cards */
.card{top:1264px;width:233px;height:240px;background:var(--white);box-shadow:0 1px 6px rgba(0,0,0,.12)}
.card__img{position:absolute;left:10px;top:10px;width:213px;height:144px}
.card__tag{position:absolute;left:10px;top:10px;background:var(--red);color:var(--white);font-size:10px;padding:2px 7px}
.card__name{position:absolute;left:10px;top:164px;font-size:14px}
.card__type{position:absolute;right:10px;top:166px;font-size:12px;color:var(--muted)}
.card__rule{position:absolute;left:10px;right:10px;top:188px;height:1px;background:var(--line)}
.card__price{position:absolute;left:10px;top:200px;width:130px;height:26px;background:var(--red);color:var(--white);font-size:11px;line-height:26px;border-radius:3px;padding-left:30px}
.card__price svg{position:absolute;left:9px;top:7px}
.card__more{position:absolute;right:10px;top:200px;width:73px;height:26px;background:#444;color:var(--white);font-size:10px;line-height:26px;text-align:center;border-radius:3px}

/* feature */
.rule-red{left:576px;top:1676px;width:48px;height:3px;background:var(--red)}
.feature__img{left:120px;top:1850px;width:565px;height:348px;background:linear-gradient(135deg,#9a9a98 0%,#7e6a5c 45%,#5d3d30 70%,#3d3b38 100%)}
.feature__box{left:645px;top:1883px;width:435px;height:280px;background:var(--panel);padding:28px 50px}
.feature__title{font-size:33px;font-weight:400}
.feature__addr{font-size:14px;line-height:18px;margin-top:18px}
.feature__meta{font-size:14px;line-height:17px;margin-top:12px}
.feature__price{font-size:15px;color:var(--red);margin-top:14px;font-weight:700}
.feature__btn{margin-top:18px;width:146px;height:38px;line-height:38px}

/* blog */
.post{top:2336px;width:300px;height:326px;border-bottom:1px solid var(--line)}
.post__img{position:absolute;left:0;top:0;width:300px;height:188px}
.post__date{position:absolute;left:12px;top:0;width:36px;height:44px;background:var(--red);color:var(--white);text-align:center;font-size:13px;line-height:15px;padding-top:6px}
.post__date small{font-size:9px;display:block}
.post__title{position:absolute;left:0;top:202px;font-size:14px;font-weight:700}
.post__meta{position:absolute;left:0;top:226px;width:300px;font-size:13px;color:var(--muted);display:flex;align-items:center;gap:5px}
.post__meta .stats{margin-left:auto;display:flex;gap:12px;align-items:center}
.post__text{position:absolute;left:0;top:250px;font-size:14px;line-height:18px}
.post__more{position:absolute;left:0;top:296px;font-size:14px;letter-spacing:1px}

/* newsletter */
.newsletter__form{left:333px;top:2852px;width:510px;height:30px;background:var(--panel);border-radius:15px;overflow:hidden}
.newsletter__field{position:absolute;left:18px;top:0;line-height:30px;font-family:var(--sans);font-size:12px;color:#999}
.newsletter__btn{position:absolute;right:0;top:0;width:130px;height:30px;background:var(--red);color:var(--white);font-size:13px;line-height:30px;text-align:center}

/* footer */
.footer{left:0;top:2946px;width:1200px;height:319px;background:var(--footer)}
.footer__about{left:122px;top:166px;width:270px;color:var(--white);font-size:13px;line-height:17px}
.footer__head{top:72px;color:var(--white);font-size:15px}
.footer__bar{top:112px;width:92px;height:2px;background:var(--white)}
.footer__links{left:455px;top:150px;color:var(--white);font-size:13px;line-height:19px;list-style:disc;padding-left:16px}
.footer__addr{left:610px;top:150px;color:var(--white);font-size:11px;line-height:14px}
.footer__addr li{display:flex;gap:10px;margin-bottom:9px;align-items:flex-start}
.footer__addr svg{flex:none;margin-top:1px}
.field{background:#444;color:#bbb;font-family:var(--sans);font-size:9px;padding:4px 8px;position:absolute}
.footer__send{left:978px;top:228px;width:102px;height:20px;background:var(--red);border-radius:10px;color:var(--white);font-size:10px;text-align:center;line-height:20px}
.footer__chat{left:936px;top:294px;width:144px;height:25px;background:var(--red);color:var(--white);border-radius:6px 6px 0 0;font-size:15px;line-height:25px;padding-left:56px}
.footer__chat svg{position:absolute;left:22px;top:6px}
.legal{left:0;top:3265px;width:1200px;height:62px;background:var(--white)}
.legal__text{left:118px;top:22px;font-size:13px;color:var(--ink)}
.legal__social{right:120px;top:19px;display:flex;gap:12px}
.legal__social span{width:24px;height:24px;border-radius:50%;background:var(--red);display:block}
</style>
</head>
<body>
<div class="page">

  <header class="abs topbar">
    <div class="abs topbar__contact topbar__mail">
      <svg width="16" height="16" viewBox="0 0 16 16"><circle cx="8" cy="8" r="7" fill="none" stroke="#222" stroke-width="1.5"/><path d="M8 4v4l3 2" fill="none" stroke="#222" stroke-width="1.5"/></svg>
      hello@tbnwrealty.com
    </div>
    <div class="abs brand brand--header"><span class="brand__mark"></span><span>TBNW</span></div>
    <div class="abs topbar__contact topbar__phone">
      <svg width="16" height="16" viewBox="0 0 16 16"><circle cx="8" cy="8" r="7" fill="none" stroke="#c4070b" stroke-width="1.5"/><path d="M5.5 4.5l1.5 0 .7 2-1 .8a5 5 0 0 0 2 2l.8-1 2 .7v1.5c-3 .5-6.5-3-6-6z" fill="#c4070b"/></svg>
      214-555-0148
    </div>
  </header>

  <nav class="abs nav">
    <a class="abs nav__item nav__item--active" style="left:122px">Home</a>
    <a class="abs nav__item" style="left:244px">Services</a>
    <a class="abs nav__item" style="left:343px">About TBNW</a>
    <a class="abs nav__item" style="left:472px">Blog</a>
    <a class="abs nav__item" style="left:549px">Contact us</a>
    <a class="abs nav__item" style="left:662px">Market News</a>
    <div class="abs nav__search">Search..
      <svg width="15" height="15" viewBox="0 0 15 15"><circle cx="6" cy="6" r="4.5" fill="none" stroke="#333" stroke-width="1.6"/><path d="M9.5 9.5l4 4" stroke="#333" stroke-width="1.8"/></svg>
    </div>
  </nav>

  <section class="abs hero" role="img" aria-label="Aerial photo of a downtown skyline with high-rise towers at dusk"></section>
  <h1 class="abs hero__title">The Best Commercial Tenant Reps<br>in Dallas TX!</h1>
  <p class="abs hero__lead">Let Us Handle Your Commercial Real Estate Lease Negotiations!</p>
  <a class="abs btn btn--hero">Read More</a>
  <div class="abs hero__dots"><span class="on"></span><span></span><span></span><span></span></div>
  <div class="abs hero__arrow" style="left:45px;top:433px"><svg width="30" height="30" viewBox="0 0 30 30"><path d="M17 10l-5 5 5 5" fill="none" stroke="#222" stroke-width="2.5"/></svg></div>
  <div class="abs hero__arrow" style="left:1125px;top:433px"><svg width="30" height="30" viewBox="0 0 30 30"><path d="M13 10l5 5-5 5" fill="none" stroke="#222" stroke-width="2.5"/></svg></div>

  <form class="abs finder">
    <div class="abs finder__select" style="left:16px;width:253px">Location<svg width="8" height="12" viewBox="0 0 8 12"><path d="M1 4l3-3 3 3M1 8l3 3 3-3" fill="none" stroke="#333" stroke-width="1.4"/></svg></div>
    <div class="abs finder__select" style="left:277px;width:195px">Category<svg width="8" height="12" viewBox="0 0 8 12"><path d="M1 4l3-3 3 3M1 8l3 3 3-3" fill="none" stroke="#333" stroke-width="1.4"/></svg></div>
    <div class="abs finder__select" style="left:482px;width:166px">Type<svg width="8" height="12" viewBox="0 0 8 12"><path d="M1 4l3-3 3 3M1 8l3 3 3-3" fill="none" stroke="#333" stroke-width="1.4"/></svg></div>
    <div class="abs finder__select" style="left:657px;width:143px">Status<svg width="8" height="12" viewBox="0 0 8 12"><path d="M1 4l3-3 3 3M1 8l3 3 3-3" fill="none" stroke="#333" stroke-width="1.4"/></svg></div>
    <div class="abs finder__go"><svg width="13" height="13" viewBox="0 0 15 15"><circle cx="6" cy="6" r="4.5" fill="none" stroke="#fff" stroke-width="1.8"/><path d="M9.5 9.5l4 4" stroke="#fff" stroke-width="2"/></svg>Search</div>
    <div class="abs finder__price">Price $ 0000 - 10000</div>
    <div class="abs finder__adv">Advance Search</div>
    <div class="abs finder__track"></div>
    <div class="abs finder__knob" style="left:16px"></div>
    <div class="abs finder__knob" style="left:924px"></div>
  </form>

  <h2 class="abs headline" style="top:870px">Professional Office and Warehouse Leasing</h2>
  <p class="abs copy" style="top:913px">Fast-track your search with tenant reps that only serve you, and specialize in the DFW area.</p>
  <h2 class="abs headline" style="top:950px">Why Tenant Representation?</h2>
  <p class="abs copy" style="top:995px">Relationships:<br>Save time by trusting TBNW year after year to find the right location for you.<br>Once we've worked together, we know what you need, and you can keep your budget details private.</p>
  <a class="abs btn btn--mid" style="top:1074px">Read More</a>

  <h2 class="abs headline" style="top:1147px">Properties</h2>
  <div class="abs tabs" style="top:1217px">
    <span class="on">All</span><i>|</i><span>House</span><i>|</i><span>Offices</span><i>|</i><span>Appartment</span><i>|</i><span>Resdential</span><i>|</i><span>Other</span>
  </div>
  <div class="abs pager" style="left:1022px">
    <span style="background:#333"><svg width="24" height="24" viewBox="0 0 24 24"><path d="M14 7l-5 5 5 5" fill="none" stroke="#fff" stroke-width="2.2"/></svg></span>
    <span style="background:var(--red)"><svg width="24" height="24" viewBox="0 0 24 24"><path d="M10 7l5 5-5 5" fill="none" stroke="#fff" stroke-width="2.2"/></svg></span>
  </div>

  <article class="abs card" style="left:113px">
    <div class="card__img" role="img" aria-label="Open land with shrubs under a cloudy sky" style="background:linear-gradient(180deg,#a9bdd2 0%,#c9d2da 45%,#6f7a5a 70%,#4e5a3b 100%)"></div>
    <span class="card__tag">Sale</span>
    <span class="card__name">Speedway</span><span class="card__type">Village</span>
    <div class="card__rule"></div>
    <span class="card__price"><svg width="13" height="12" viewBox="0 0 13 12"><path d="M0 1h2l2 7h7l1.5-5H3" fill="none" stroke="#fff" stroke-width="1.4"/><circle cx="5" cy="10.5" r="1.2" fill="#fff"/><circle cx="10" cy="10.5" r="1.2" fill="#fff"/></svg>$30,730,035.40</span>
    <span class="card__more">Read More</span>
  </article>
  <article class="abs card" style="left:361px">
    <div class="card__img" role="img" aria-label="Carpeted office interior with a sofa" style="background:linear-gradient(160deg,#d8d2c4 0%,#a99e88 50%,#6c6455 100%)"></div>
    <span class="card__tag">Sale</span>
    <span class="card__name">Parkway Office</span><span class="card__type">House</span>
    <div class="card__rule"></div>
    <span class="card__price"><svg width="13" height="12" viewBox="0 0 13 12"><path d="M0 1h2l2 7h7l1.5-5H3" fill="none" stroke="#fff" stroke-width="1.4"/><circle cx="5" cy="10.5" r="1.2" fill="#fff"/><circle cx="10" cy="10.5" r="1.2" fill="#fff"/></svg>$19.50</span>
    <span class="card__more">Read More</span>
  </article>
  <article class="abs card" style="left:609px">
    <div class="card__img" role="img" aria-label="Conference room with a long table and chairs" style="background:linear-gradient(180deg,#c9cbcc 0%,#8b8e90 55%,#3d3f41 100%)"></div>
    <span class="card__tag">Sale</span>
    <span class="card__name">Turtle Creek</span><span class="card__type">Office</span>
    <div class="card__rule"></div>
    <span class="card__price"><svg width="13" height="12" viewBox="0 0 13 12"><path d="M0 1h2l2 7h7l1.5-5H3" fill="none" stroke="#fff" stroke-width="1.4"/><circle cx="5" cy="10.5" r="1.2" fill="#fff"/><circle cx="10" cy="10.5" r="1.2" fill="#fff"/></svg>$32.00</span>
    <span class="card__more">Read More</span>
  </article>
  <article class="abs card" style="left:858px">
    <div class="card__img" role="img" aria-label="Low white studio building under a blue sky" style="background:linear-gradient(180deg,#2f6bc2 0%,#6e9bd6 40%,#e6e2da 62%,#b9aa92 100%)"></div>
    <span class="card__tag">Sale</span>
    <span class="card__name">Media Production Studio</span>
    <div class="card__rule"></div>
    <span class="card__price"><svg width="13" height="12" viewBox="0 0 13 12"><path d="M0 1h2l2 7h7l1.5-5H3" fill="none" stroke="#fff" stroke-width="1.4"/><circle cx="5" cy="10.5" r="1.2" fill="#fff"/><circle cx="10" cy="10.5" r="1.2" fill="#fff"/></svg>$1,902,535.00</span>
    <span class="card__more">Read More</span>
  </article>

  <a class="abs btn btn--mid" style="top:1540px">View More</a>

  <h2 class="abs headline" style="top:1628px">Dimensions</h2>
  <div class="abs rule-red"></div>
  <p class="abs copy" style="top:1699px">Lorem Ipsum is simply dummy text of the printing matter<br>and typesetting industry.</p>
  <div class="abs tabs" style="top:1766px">
    <span class="on">House</span><i>|</i><span>Offices</span><i>|</i><span>Appartment</span><i>|</i><span>Resdential</span><i>|</i><span>Village</span><i>|</i><span>Flat</span><i>|</i><span>Other</span>
  </div>

  <div class="abs feature__img" role="img" aria-label="Grey clapboard townhouse with a red front door and a bicycle by the steps"></div>
  <div class="abs feature__box">
    <h3 class="feature__title">House</h3>
    <p class="feature__addr">4820 Meridian Parkway Office Sublease Addison,<br>Texas 75001</p>
    <p class="feature__meta">Category: Office Space Sublease<br>Tag: office sublease</p>
    <p class="feature__price">$19.50</p>
    <a class="btn feature__btn">Read More</a>
  </div>

  <h2 class="abs headline" style="top:2256px">Our Blog</h2>
  <p class="abs copy" style="top:2302px">Lorem Ipsum is simply dummy text.</p>

  <article class="abs post" style="left:120px">
    <div class="post__img" role="img" aria-label="Bright open-plan office with white desks" style="background:linear-gradient(160deg,#f2f3f4 0%,#cfd3d6 50%,#8f969b 100%)"></div>
    <div class="post__date">08<small>May</small></div>
    <h4 class="post__title">Do You Need Office Space?</h4>
    <div class="post__meta"><svg width="11" height="11" viewBox="0 0 11 11"><rect x="1" y="2" width="9" height="8" fill="none" stroke="#555"/><path d="M1 4.5h9" stroke="#555"/></svg>May 04, 2018<span class="stats"><span>&#9675; 20</span><span>&#9825; 12</span></span></div>
    <p class="post__text">Lorem Ipsum is simply dummy text of the<br>printing matter and typesetting industry.</p>
    <span class="post__more">Read More &#9675;</span>
  </article>
  <article class="abs post" style="left:450px">
    <div class="post__img" role="img" aria-label="Business people walking through a shared office lobby" style="background:linear-gradient(160deg,#e4d6bf 0%,#b09a7a 50%,#5e5246 100%)"></div>
    <div class="post__date">07<small>May</small></div>
    <h4 class="post__title">Shared Building Amenities</h4>
    <div class="post__meta"><svg width="11" height="11" viewBox="0 0 11 11"><rect x="1" y="2" width="9" height="8" fill="none" stroke="#555"/><path d="M1 4.5h9" stroke="#555"/></svg>May 03, 2018<span class="stats"><span>&#9675; 20</span><span>&#9825; 12</span></span></div>
    <p class="post__text">Lorem Ipsum is simply dummy text of the<br>printing matter and typesetting industry.</p>
    <span class="post__more">Read More &#9675;</span>
  </article>
  <article class="abs post" style="left:780px">
    <div class="post__img" role="img" aria-label="Commercial lease document with a pen and banknotes" style="background:linear-gradient(160deg,#8a3a22 0%,#d8cfc2 35%,#efece6 60%,#8c9a7a 100%)"></div>
    <div class="post__date">06<small>May</small></div>
    <h4 class="post__title">Entering Into A Commercial Lease?</h4>
    <div class="post__meta"><svg width="11" height="11" viewBox="0 0 11 11"><rect x="1" y="2" width="9" height="8" fill="none" stroke="#555"/><path d="M1 4.5h9" stroke="#555"/></svg>May 02, 2018<span class="stats"><span>&#9675; 20</span><span>&#9825; 12</span></span></div>
    <p class="post__text">Lorem Ipsum is simply dummy text of the<br>printing matter and typesetting industry.</p>
    <span class="post__more">Read More &#9675;</span>
  </article>

  <a class="abs btn btn--mid" style="top:2696px">Read More</a>

  <h2 class="abs headline" style="top:2782px;font-size:22px">Join The Newletter</h2>
  <p class="abs copy" style="top:2815px">Sign up for Our Newsletter</p>
  <form class="abs newsletter__form">
    <span class="newsletter__field">Email here</span>
    <span class="newsletter__btn">Subscribe</span>
  </form>

  <footer class="abs footer">
    <div class="abs brand brand--footer"><span class="brand__mark"></span><span>TBNW</span></div>
    <p class="abs footer__about">Lorem Ipsum is simply dummy text the printing and ypesetting industry. has been the industry's standard dummy..</p>

    <h5 class="abs footer__head" style="left:455px">Quick Link</h5>
    <div class="abs footer__bar" style="left:455px"></div>
    <ul class="abs footer__links">
      <li>Home</li><li>Services</li><li>About TBNW</li><li>Blog</li><li>Contact us</li><li>Market News</li>
    </ul>

    <h5 class="abs footer__head" style="left:632px">Address</h5>
    <div class="abs footer__bar" style="left:632px"></div>
    <ul class="abs footer__addr">
      <li><svg width="11" height="14" viewBox="0 0 11 14"><path d="M5.5 13C2 8.5 1 7 1 5a4.5 4.5 0 0 1 9 0c0 2-1 3.5-4.5 8z" fill="#fff"/><circle cx="5.5" cy="5" r="1.6" fill="#2f2f2f"/></svg><span>1200 Elm Ridge Avenue, Suite 410,<br>Dallas, TX 75201.</span></li>
      <li><svg width="12" height="12" viewBox="0 0 12 12"><path d="M2 1h2.5l1 3-1.5 1a6 6 0 0 0 3 3l1-1.5 3 1V10c-5 1-10-4-9-9z" fill="#fff"/></svg><span>Tel: 214-555-0172 |</span></li>
      <li><svg width="12" height="12" viewBox="0 0 12 12"><rect x="1" y="4" width="10" height="6" fill="#fff"/><rect x="3" y="1" width="6" height="3" fill="#fff"/></svg><span>Fax: 214-555-0173</span></li>
      <li><svg width="12" height="10" viewBox="0 0 12 10"><rect x=".5" y=".5" width="11" height="9" fill="none" stroke="#fff"/><path d="M.5 .5l5.5 5 5.5-5" fill="none" stroke="#fff"/></svg><span>hello@tbnwrealty.com</span></li>
    </ul>

    <h5 class="abs footer__head" style="left:847px">Quick Contact</h5>
    <div class="abs footer__bar" style="left:847px"></div>
    <span class="field" style="left:847px;top:137px;width:112px;height:20px">Name</span>
    <span class="field" style="left:968px;top:137px;width:112px;height:20px">Phone</span>
    <span class="field" style="left:847px;top:164px;width:233px;height:50px">Message</span>
    <span class="abs footer__send">SEND</span>

    <div class="abs footer__chat"><svg width="16" height="14" viewBox="0 0 16 14"><path d="M1 1h14v9H6l-4 3v-3H1z" fill="#fff"/></svg>Live Chat</div>
  </footer>

  <div class="abs legal">
    <p class="abs legal__text">Copyright © 2018 TBNW Brennick Commercial Realty Group. All Rights Reserved.</p>
    <div class="abs legal__social"><span></span><span></span><span></span><span></span><span></span></div>
  </div>

</div>
</body>
</html>
```